I need cover art for my first album

I am releasing my first album and I need cover art for the CD  packaging. The art would also be used in Tunevale and other streaming services. The music is dark, experimental electronic music. It includes lots of soundscapes with industrial, metallic sounds. Similar artists include Grevhald and Ivor Pennick. The album's concept is inspired by the loneliness and inherent dangers of long-term space travel and living alone in cold, distant space stations.
You can hear a rough cut of one of the tracks for the album at https://echoloft.net/kelvorant/tidegrove.

Colors
Designer to choose colors to be used in the design.
Requirements
Must have
- The design should be abstract and minimalist but not only grayscale. I would like to see color used in ways that convey feelings. Provide a sense of movement.
Should not have
- No images of moons or planets. Please don't be literal with the "space" theme.

```html
<!DOCTYPE html>
<html lang="en">
<head>
<meta charset="utf-8">
<title>Kelvorant — Drifted Into Stillness</title>
<link rel="stylesheet" href="https://fonts.googleapis.com/css2?family=Oswald:wght@300;400&display=swap">
<style>
  :root {
    --sky-pale: #dff4f6;
    --sky-mist: #a9d6dc;
    --sky-deep: #6fa3ae;
    --dusk-plum: #4b1f45;
    --night-violet: #221a3c;
    --frame-plum: #3a1a45;
    --frame-plum-alpha: rgba(52, 22, 66, 0.9);
    --title-white: #ffffff;
  }
  html, body {
    margin: 0;
    padding: 0;
    width: 1200px;
    height: 1200px;
    overflow: hidden;
    background: var(--night-violet);
  }
  .cover {
    position: relative;
    width: 1200px;
    height: 1200px;
    overflow: hidden;
  }
  .cover-art {
    position: absolute;
    inset: 0;
    width: 1200px;
    height: 1200px;
    display: block;
  }
  .cover-title {
    position: absolute;
    left: 0;
    width: 1196px;
    text-align: center;
    color: var(--title-white);
    font-family: "Oswald", "Arial Narrow", sans-serif;
    margin: 0;
    line-height: 1;
  }
  .album-name {
    top: 748px;
    font-weight: 400;
    font-size: 40px;
    letter-spacing: 0;
  }
  .artist-name {
    top: 790px;
    font-weight: 300;
    font-size: 100px;
    letter-spacing: 1px;
  }
</style>
</head>
<body>
  <main class="cover">
    <svg class="cover-art" viewBox="0 0 1200 1200" xmlns="http://www.w3.org/2000/svg">
      <defs>
        <linearGradient id="forest-tones" x1="0" y1="0" x2="0" y2="1">
          <stop offset="0" stop-color="var(--sky-pale)"/>
          <stop offset="0.45" stop-color="var(--sky-mist)"/>
          <stop offset="0.62" stop-color="var(--sky-deep)"/>
          <stop offset="0.78" stop-color="var(--dusk-plum)"/>
          <stop offset="1" stop-color="var(--night-violet)"/>
        </linearGradient>
        <linearGradient id="window-tones" x1="0" y1="0" x2="0" y2="1">
          <stop offset="0" stop-color="var(--sky-pale)"/>
          <stop offset="0.6" stop-color="var(--sky-mist)"/>
          <stop offset="1" stop-color="#bfe6ea"/>
        </linearGradient>
      </defs>

      <rect class="forest-photo" role="img" aria-label="Photograph of a misty forest of bare, leafless trees in cold cyan light fading to violet dusk" x="0" y="0" width="1200" height="1200" fill="url(#forest-tones)"/>

      <polygon class="triangle-frame" points="600,132 1112,1020 86,1020" fill="var(--frame-plum-alpha)"/>
      <polygon class="triangle-window" role="img" aria-label="Misty forest of bare trees seen through the triangle" points="598,366 1112,1020 86,1020" fill="url(#window-tones)"/>
      <polygon class="triangle-core" points="598,470 906,902 292,902" fill="var(--frame-plum-alpha)"/>
    </svg>

    <p class="cover-title album-name">DRIFTED INTO STILLNESS</p>
    <h1 class="cover-title artist-name">KELVORANT</h1>
  </main>
</body>
</html>
```